A4 Client Referral Program Flyer for Property Management Agency

Harbourleaf Estates Agency is a property management specialist based on Sydney's Northern Beaches in Australia.

We manage mid to high-end rental properties for investors and property owners.
We are currently looking to build our portfolio and are offering existing clients and contacts a referral incentive. We want to sign up more properties to manage.

We are offering the referrer a $250 referral fee and the new owner 2 months of free management to entice them to use Harbourleaf Estates Agency.

We want an A4 Flyer to print and add to other document packages we hand out to clients and suppliers.
If at all possible a matching digital banner would be great too! 1000px wide x 250px

Please find copy attached in Word Doc and our logo attached also.

Please see our website for any more details on our business.

We must be able to have an editable photoshop version (PSD) of the document as well as a print ready PDF version incl any bleed necessary for A4 printing.

Target Market(s)

30-60YO Male and Female

Industry/Entity Type

Real Estate

Font styles to use
Sans Serif

Requirements
Must have
• Company Logo, contact details and copy provided

```html
<!DOCTYPE html>
<html lang="en">
<head>
<meta charset="utf-8">
<title>Harbourleaf Estates Agency – Referral Flyer and Banner</title>
<link href="https://fonts.googleapis.com/css2?family=Oswald:wght@300;400&family=Roboto+Condensed:wght@400;700&family=Montserrat:wght@800&display=swap" rel="stylesheet">
<style>
  :root {
    --page: #ecebe8;
    --ink: #16171b;
    --dark: #1b1c20;
    --cyan: #2ad4df;
    --cyan-light: #6ff0f5;
    --navy: #1c1a5c;
    --white: #ffffff;
    --muted: #e6e8ea;
  }
  * { margin: 0; padding: 0; box-sizing: border-box; }
  html, body { width: 1200px; height: 1200px; overflow: hidden; }
  body { background: var(--page); font-family: "Roboto Condensed", sans-serif; position: relative; }

  .flyer, .banner { position: absolute; overflow: hidden; background: var(--dark); box-shadow: 0 4px 14px rgba(0,0,0,.25); }
  .flyer { left: 42px; top: 46px; width: 626px; height: 886px; }
  .banner { left: 366px; top: 972px; width: 800px; height: 200px; }
  .art { position: absolute; inset: 0; }

  .brand { position: absolute; color: var(--ink); font-family: "Roboto Condensed", sans-serif; font-weight: 700; line-height: 1; }
  .flyer .brand { left: 16px; top: 84px; font-size: 31px; }
  .banner .brand { left: 4px; top: 40px; font-size: 16px; line-height: 1.05; }

  .offer { position: absolute; }
  .offer-word { font-family: "Montserrat", sans-serif; font-weight: 800; color: var(--navy); }
  .offer-copy { position: absolute; color: var(--navy); font-weight: 700; text-transform: uppercase; line-height: 1.2; }
  .offer-copy .big { font-size: 1.45em; display: block; }
  .offer-copy .gap { display: block; height: .7em; }

  .flyer .offer { left: 370px; top: 370px; width: 226px; height: 208px; }
  .flyer .offer-word { position: absolute; left: 6px; top: 6px; font-size: 48px; letter-spacing: 10px; line-height: 1; }
  .flyer .offer-copy { left: 76px; top: 76px; font-size: 12px; }

  .banner .offer { left: 328px; top: 18px; width: 174px; height: 164px; }
  .banner .offer-word { position: absolute; left: 6px; bottom: 4px; font-size: 32px; letter-spacing: 6px; line-height: 1; transform-origin: left bottom; transform: rotate(-90deg) translateY(100%); white-space: nowrap; }
  .banner .offer-copy { left: 58px; top: 72px; font-size: 8.6px; }

  .info { position: absolute; color: var(--white); }
  .fee { font-family: "Oswald", sans-serif; font-weight: 400; color: var(--cyan); line-height: 1; white-space: nowrap; }
  .terms { color: var(--muted); line-height: 1.45; }
  .link { color: var(--cyan); display: flex; align-items: center; gap: 6px; white-space: nowrap; }
  .link svg { flex: none; }
  .phone { font-family: "Oswald", sans-serif; font-weight: 400; color: var(--white); line-height: 1; white-space: nowrap; }
  .contact { display: flex; align-items: center; gap: 8px; color: var(--cyan); white-space: nowrap; }
  .contact .plain { color: var(--white); }

  .flyer .info { left: 250px; top: 598px; width: 352px; }
  .flyer .fee { font-size: 44px; letter-spacing: -.3px; }
  .flyer .terms { font-size: 12.2px; margin: 24px 0 0 20px; }
  .flyer .link { font-size: 14px; margin: 8px 0 0 2px; }
  .flyer .phone { font-size: 62px; letter-spacing: 3px; margin-top: 12px; }
  .flyer .contact { font-size: 20px; margin-top: 4px; }

  .banner .info { left: 556px; top: 13px; width: 236px; }
  .banner .fee { font-size: 28px; letter-spacing: -.3px; }
  .banner .terms { font-size: 7.4px; margin: 14px 0 0 12px; line-height: 1.35; }
  .banner .link { font-size: 8.6px; margin: 5px 0 0 0; gap: 4px; }
  .banner .phone { font-size: 38px; letter-spacing: 2px; margin-top: 5px; }
  .banner .contact { font-size: 12.5px; margin-top: 1px; gap: 5px; }
</style>
</head>
<body>

<section class="flyer" aria-label="Referral program flyer">
  <svg class="art" viewBox="0 0 626 886" width="626" height="886">
    <defs>
      <linearGradient id="flyer-scene" x1="0" y1="0" x2="0" y2="1">
        <stop offset="0" stop-color="#f7f7fa"/>
        <stop offset=".25" stop-color="#e8dfe6"/>
        <stop offset=".45" stop-color="#7a8092"/>
        <stop offset=".7" stop-color="#a4a7ad"/>
        <stop offset="1" stop-color="#6b5f57"/>
      </linearGradient>
      <linearGradient id="garden" x1="0" y1="0" x2="0" y2="1">
        <stop offset="0" stop-color="#dfe6ea"/><stop offset="1" stop-color="#4f8a3c"/>
      </linearGradient>
      <linearGradient id="pool" x1="0" y1="0" x2="0" y2="1">
        <stop offset="0" stop-color="#6fb6ea"/><stop offset=".5" stop-color="#5f8a4c"/><stop offset="1" stop-color="#27a6d8"/>
      </linearGradient>
      <linearGradient id="keys" x1="0" y1="0" x2="0" y2="1">
        <stop offset="0" stop-color="#2d3530"/><stop offset=".6" stop-color="#b5b043"/><stop offset="1" stop-color="#8fc23a"/>
      </linearGradient>
      <linearGradient id="offer-fill" x1="0" y1="0" x2="1" y2="1">
        <stop offset="0" stop-color="#2ad4df"/><stop offset="1" stop-color="#6ff0f5"/>
      </linearGradient>
    </defs>

    <rect width="626" height="886" fill="url(#flyer-scene)" role="img" aria-label="Photo of a two-storey weatherboard home with a modern house and garden at left"/>

    <path d="M300 341 H626 V356 H330 C190 500 130 700 112 886 H88 C108 700 170 480 300 341 Z" fill="var(--cyan)"/>
    <path d="M330 356 H626 V886 H112 C130 700 190 500 330 356 Z" fill="var(--dark)"/>

    <g>
      <circle cx="249" cy="369" r="90" fill="#ffffff"/>
      <circle cx="249" cy="369" r="84" fill="var(--cyan)"/>
      <circle cx="249" cy="369" r="72" fill="url(#garden)" role="img" aria-label="Photo of a white home with front stairs and garden"/>
    </g>
    <g>
      <circle cx="136" cy="545" r="74" fill="#ffffff"/>
      <circle cx="136" cy="545" r="69" fill="var(--cyan)"/>
      <circle cx="136" cy="545" r="59" fill="url(#pool)" role="img" aria-label="Photo of a resort pool with palm trees"/>
    </g>
    <g>
      <circle cx="109" cy="718" r="62" fill="#ffffff"/>
      <circle cx="109" cy="718" r="57" fill="var(--cyan)"/>
      <circle cx="109" cy="718" r="48" fill="url(#keys)" role="img" aria-label="Photo of a small model house passed between hands"/>
    </g>

    <path d="M370 370 H596 V552 L483 590 L370 552 Z" fill="url(#offer-fill)"/>
    <line x1="374" y1="373" x2="592" y2="373" stroke="var(--navy)" stroke-width="2"/>
    <line x1="374" y1="424" x2="592" y2="424" stroke="var(--navy)" stroke-width="1.5"/>
    <path d="M386 438 H408 V518 H422 L397 546 L372 518 H386 Z" fill="#ffffff"/>
  </svg>

  <p class="brand">HARBOURLEAF ESTATES<br>AGENCY</p>

  <div class="offer">
    <p class="offer-word">OFFER</p>
    <p class="offer-copy">Invite your friends &amp;<span class="gap"></span><span class="big">Receive $250</span>and they get<span class="gap"></span>2 months free<br>management! *</p>
  </div>

  <div class="info">
    <p class="fee">*$250 REFERRAL FEE</p>
    <p class="terms">Paid when the owner you refer signs their property for Management with Harbourleaf Estates Agency. Your referral must be submitted prior to signing on our website using the referral form on this page:</p>
    <p class="link"><svg width="14" height="14" viewBox="0 0 14 14"><circle cx="7" cy="7" r="5.5" fill="none" stroke="var(--cyan)" stroke-width="1.6"/><path d="M7 7 L12 12" stroke="var(--cyan)" stroke-width="1.6"/></svg>www.harbourleafestates.com.au/referral-program</p>
    <p class="phone">0400 555 182</p>
    <p class="contact"><svg width="22" height="22" viewBox="0 0 22 22"><circle cx="11" cy="11" r="9.5" fill="none" stroke="var(--cyan)" stroke-width="1.6"/><ellipse cx="11" cy="11" rx="4" ry="9.5" fill="none" stroke="var(--cyan)" stroke-width="1.4"/><path d="M1.5 11 H20.5 M3.5 6 H18.5 M3.5 16 H18.5" stroke="var(--cyan)" stroke-width="1.4"/></svg><span>www.<span class="plain">harbourleafestates</span>.com.au</span></p>
    <p class="contact"><svg width="22" height="16" viewBox="0 0 22 16"><rect x="1" y="1" width="20" height="14" fill="var(--cyan)"/><path d="M1 1 L11 9 L21 1" fill="none" stroke="var(--dark)" stroke-width="1.6"/></svg><span>referrals@<span class="plain">harbourleafestates</span>.com.au</span></p>
  </div>
</section>

<section class="banner" aria-label="Referral program web banner">
  <svg class="art" viewBox="0 0 800 200" width="800" height="200">
    <defs>
      <linearGradient id="banner-scene" x1="0" y1="0" x2="0" y2="1">
        <stop offset="0" stop-color="#f4f5f8"/>
        <stop offset=".45" stop-color="#c9ccd6"/>
        <stop offset=".75" stop-color="#6f7890"/>
        <stop offset="1" stop-color="#4a4f5a"/>
      </linearGradient>
      <linearGradient id="b-garden" x1="0" y1="0" x2="0" y2="1">
        <stop offset="0" stop-color="#dfe6ea"/><stop offset="1" stop-color="#4f8a3c"/>
      </linearGradient>
      <linearGradient id="b-pool" x1="0" y1="0" x2="0" y2="1">
        <stop offset="0" stop-color="#6fb6ea"/><stop offset=".5" stop-color="#5f8a4c"/><stop offset="1" stop-color="#27a6d8"/>
      </linearGradient>
      <linearGradient id="b-keys" x1="0" y1="0" x2="0" y2="1">
        <stop offset="0" stop-color="#2d3530"/><stop offset=".6" stop-color="#b5b043"/><stop offset="1" stop-color="#8fc23a"/>
      </linearGradient>
      <linearGradient id="b-offer" x1="0" y1="0" x2="1" y2="1">
        <stop offset="0" stop-color="#2ad4df"/><stop offset="1" stop-color="#6ff0f5"/>
      </linearGradient>
    </defs>

    <rect width="320" height="200" fill="url(#banner-scene)" role="img" aria-label="Photo of a two-storey home with garage beside a modern house"/>
    <path d="M248 0 C262 60 282 130 312 200 H320 V0 Z" fill="var(--cyan)"/>
    <path d="M256 0 C270 60 290 130 320 200 H800 V0 Z" fill="var(--dark)"/>

    <circle cx="230" cy="32" r="34" fill="#ffffff"/>
    <circle cx="230" cy="32" r="31" fill="var(--cyan)"/>
    <circle cx="230" cy="32" r="26" fill="url(#b-garden)" role="img" aria-label="Photo of a white home with garden"/>
    <circle cx="242" cy="112" r="29" fill="#ffffff"/>
    <circle cx="242" cy="112" r="26" fill="var(--cyan)"/>
    <circle cx="242" cy="112" r="22" fill="url(#b-pool)" role="img" aria-label="Photo of a resort pool"/>
    <circle cx="282" cy="168" r="23" fill="#ffffff"/>
    <circle cx="282" cy="168" r="20.5" fill="var(--cyan)"/>
    <circle cx="282" cy="168" r="17" fill="url(#b-keys)" role="img" aria-label="Photo of a model house passed between hands"/>

    <path d="M328 18 H476 L502 100 L476 182 H328 Z" fill="url(#b-offer)"/>
    <line x1="376" y1="22" x2="376" y2="178" stroke="var(--navy)" stroke-width="1.5"/>
    <path d="M388 38 H416 V28 L438 46 L416 64 V54 H388 Z" fill="#ffffff"/>
  </svg>

  <p class="brand">HARBOURLEAF ESTATES<br>AGENCY</p>

  <div class="offer">
    <p class="offer-word">OFFER</p>
    <p class="offer-copy">Invite your friends &amp;<span class="gap"></span><span class="big">Receive $250</span>and they get<span class="gap"></span>2 months free<br>management! *</p>
  </div>

  <div class="info">
    <p class="fee">*$250 REFERRAL FEE</p>
    <p class="terms">Paid when the owner you refer signs their property for Management with Harbourleaf Estates Agency. Your referral must be submitted prior to signing on our website using the referral form on this page:</p>
    <p class="link"><svg width="9" height="9" viewBox="0 0 14 14"><circle cx="7" cy="7" r="5.5" fill="none" stroke="var(--cyan)" stroke-width="1.8"/><path d="M7 7 L12 12" stroke="var(--cyan)" stroke-width="1.8"/></svg>www.harbourleafestates.com.au/referral-program</p>
    <p class="phone">0400 555 182</p>
    <p class="contact"><svg width="13" height="13" viewBox="0 0 22 22"><circle cx="11" cy="11" r="9.5" fill="none" stroke="var(--cyan)" stroke-width="1.8"/><ellipse cx="11" cy="11" rx="4" ry="9.5" fill="none" stroke="var(--cyan)" stroke-width="1.6"/><path d="M1.5 11 H20.5" stroke="var(--cyan)" stroke-width="1.6"/></svg><span>www.<span class="plain">harbourleafestates</span>.com.au</span></p>
    <p class="contact"><svg width="13" height="10" viewBox="0 0 22 16"><rect x="1" y="1" width="20" height="14" fill="var(--cyan)"/><path d="M1 1 L11 9 L21 1" fill="none" stroke="var(--dark)" stroke-width="1.8"/></svg><span>referrals@<span class="plain">harbourleafestates</span>.com.au</span></p>
  </div>
</section>

</body>
</html>
```